Velmoro Consulting Business

** Please add the content information from my old business card
1. I would like to see a two sided business card with both options with the 1st Option--Sketch Nest-new WHITE BACKGROUND LOGO
2 nd Option-Sketch Nest - new BLACK- Background Logo
3rd -Option a business card with my Photo on the card
Please add the new word to the card information:
EXECUTION
AS THE OWNER'S REP
WE AIM TO ACHIEVE YOUR
INFRASTRUCTURE VISION with
OUR SPECIALIZATION & EXECUTION in:

FUNDING Planning
BUSINESS Planning
INFRASTRUCTURE Planning
PROJECT Management
Since 2012
_____________________________________________________________________
I want to get spot uv raised printing. I was liking a a nice rich white linen paper stock with black writing & NOT A COLORED CARD other than a variety of white or black cards concept

```html
<!DOCTYPE html>
<html lang="en">
<head>
<meta charset="utf-8">
<title>Velmoro Consulting – Business Cards</title>
<link rel="stylesheet" href="https://fonts.googleapis.com/css2?family=Lato:wght@300;400;700;900&display=swap">
<style>
  :root {
    --stage: #2b2b2d;
    --card-black: #1e1e1f;
    --card-white: #eeeeee;
    --ink: #1a1a1a;
    --paper-text: #ffffff;
    --muted: #8a8a8a;
    --accent: #e8213a;
  }
  * { box-sizing: border-box; margin: 0; padding: 0; }
  html, body { width: 1200px; height: 799px; overflow: hidden; }
  body {
    background: var(--stage);
    font-family: "Lato", sans-serif;
    position: relative;
  }
  .card {
    position: absolute;
    width: 540px;
    height: 309px;
    border-radius: 3px;
    box-shadow: 0 14px 30px rgba(0,0,0,.45);
    overflow: hidden;
  }

  /* Back side – black stock */
  .card--back {
    left: 40px; top: 130px;
    background: var(--card-black);
    color: var(--paper-text);
  }
  .brand {
    position: absolute;
    display: flex;
    flex-direction: column;
  }
  .card--back .brand { left: 34px; bottom: 40px; }
  .brand__name {
    font-weight: 900;
    font-size: 40px;
    letter-spacing: -1px;
    line-height: 1;
  }
  .brand__tag {
    font-weight: 400;
    font-size: 11px;
    letter-spacing: 11px;
    text-transform: uppercase;
    margin-top: 6px;
  }
  .card--back .brand__name { color: #4a4a4c; }
  .card--back .brand__tag { color: var(--muted); }

  .mission {
    position: absolute;
    left: 270px; top: 34px;
    font-weight: 700;
    font-size: 11.5px;
    line-height: 1.45;
    text-transform: uppercase;
    letter-spacing: .3px;
  }
  .mission .lower { text-transform: none; }
  .rule {
    width: 48px; height: 2px;
    background: var(--accent);
    margin: 8px 0 8px;
  }
  .services { list-style: none; font-size: 11.5px; line-height: 1.5; }
  .services b { font-weight: 700; letter-spacing: .3px; }
  .services span { font-weight: 300; }
  .since {
    position: absolute;
    right: 26px; bottom: 24px;
    font-size: 10px;
    font-weight: 400;
    color: #d8d8d8;
  }

  /* Front side – white linen stock */
  .card--front {
    left: 620px; top: 360px;
    background:
      repeating-linear-gradient(0deg, rgba(0,0,0,.025) 0 1px, transparent 1px 3px),
      repeating-linear-gradient(90deg, rgba(0,0,0,.025) 0 1px, transparent 1px 3px),
      var(--card-white);
    color: var(--ink);
  }
  .card--front .brand { right: 34px; top: 30px; align-items: flex-end; }
  .card--front .brand__name { color: var(--ink); font-size: 42px; }
  .card--front .brand__tag { color: var(--ink); }

  .person {
    position: absolute;
    right: 34px; top: 118px;
    text-align: right;
  }
  .person__name { font-weight: 900; font-size: 19px; }
  .person__role {
    font-weight: 400; font-size: 10.5px;
    color: var(--accent);
    text-transform: uppercase;
    letter-spacing: .4px;
    margin-top: 2px;
  }
  .contact {
    position: absolute;
    right: 34px; top: 184px;
    list-style: none;
    font-size: 11px;
    line-height: 1.55;
    text-align: right;
  }
  .contact li { display: flex; align-items: center; justify-content: flex-end; gap: 7px; }
  .contact svg { width: 9px; height: 9px; fill: var(--accent); flex: none; }
  .accent-bar {
    position: absolute;
    right: 0; top: 122px;
    width: 8px; height: 40px;
    background: var(--accent);
  }
</style>
</head>
<body>

<section class="card card--back" aria-label="Business card back">
  <div class="brand">
    <span class="brand__name">Velmoro</span>
    <span class="brand__tag">Consulting</span>
  </div>

  <div class="mission">
    <p>Execution</p>
    <p>As the owner's rep</p>
    <p>We aim to achieve your</p>
    <p>Infrastructure vision <span class="lower">with</span></p>
    <p>Our specialization &amp; execution <span class="lower">in:</span></p>
    <div class="rule"></div>
    <ul class="services">
      <li><b>FUNDING</b> <span>Planning</span></li>
      <li><b>BUSINESS</b> <span>Planning</span></li>
      <li><b>INFRASTRUCTURE</b> <span>Planning</span></li>
      <li><b>PROJECT</b> <span>Management</span></li>
    </ul>
  </div>

  <p class="since">Since 2012</p>
</section>

<section class="card card--front" aria-label="Business card front">
  <div class="brand">
    <span class="brand__name">Velmoro</span>
    <span class="brand__tag">Consulting</span>
  </div>

  <div class="person">
    <p class="person__name">Marissa Corliss-Vantan</p>
    <p class="person__role">CEO / Lead Project Manager</p>
  </div>
  <div class="accent-bar"></div>

  <ul class="contact">
    <li>555.014.2290
      <svg viewBox="0 0 10 10" aria-hidden="true"><rect x="2.5" y="0" width="5" height="10" rx="1"/></svg></li>
    <li>mari@velmoro.ca
      <svg viewBox="0 0 10 10" aria-hidden="true"><path d="M0 2h10v6H0z"/></svg></li>
    <li>www.velmoro.ca
      <svg viewBox="0 0 10 10" aria-hidden="true"><circle cx="5" cy="5" r="5"/></svg></li>
    <li>Harrowmere NT
      <svg viewBox="0 0 10 10" aria-hidden="true"><path d="M5 0a3.5 3.5 0 0 1 3.5 3.5C8.5 6 5 10 5 10S1.5 6 1.5 3.5A3.5 3.5 0 0 1 5 0z"/></svg></li>
    <li>Linbrook NB
      <svg viewBox="0 0 10 10" aria-hidden="true"><path d="M5 0a3.5 3.5 0 0 1 3.5 3.5C8.5 6 5 10 5 10S1.5 6 1.5 3.5A3.5 3.5 0 0 1 5 0z"/></svg></li>
  </ul>
</section>

</body>
</html>
```